Engineering Consultant Business Card

I'm starting a new business as a high-end engineering consultant in a niche field. I've attached the jpg for my logo plus the branding guideline document that I've been following. You can see my business website here: www.tarvikworks.com
I'd like a business card that has the logo on one side, then the other side has (in any order): Tarvik Works, Inc.
Dana Whitlock
President and Chief EMC Engineer
www.tarvikworks.com
dana@tarvikworks.com
Optional: motto "We will solve your EMC problems as early as possible—ideally before they even start."
I'm not planning on including a phone number
Target Market(s)
Businesses, especially makers of electronics hardware
Industry/Entity Type
Electrical engineering
Contact Information for Business Card
Company name, my name, website, email

```html
<!DOCTYPE html>
<html lang="en">
<head>
<meta charset="utf-8">
<title>Tarvik Works, Inc. — Business Card</title>
<link rel="stylesheet" href="https://fonts.googleapis.com/css2?family=Roboto:wght@400;500;700&display=swap">
<style>
  :root {
    --brand-blue: #2f4597;
    --ink: #1f1f24;
    --paper: #ffffff;
    --backdrop: #e9e9ea;
    --card-shadow: 0 18px 30px rgba(0, 0, 0, 0.22), 0 4px 8px rgba(0, 0, 0, 0.08);
  }
  * { box-sizing: border-box; margin: 0; padding: 0; }
  html, body {
    width: 1200px;
    height: 1200px;
    overflow: hidden;
    background: var(--backdrop);
    font-family: "Roboto", Arial, sans-serif;
  }
  .canvas {
    position: relative;
    width: 1200px;
    height: 1200px;
  }
  .card {
    position: absolute;
    top: 453px;
    width: 490px;
    height: 294px;
    box-shadow: var(--card-shadow);
    overflow: hidden;
  }
  .card--front {
    left: 83px;
    background: var(--brand-blue);
    display: flex;
    align-items: center;
    justify-content: center;
  }
  .brand-mark {
    display: flex;
    align-items: center;
    gap: 14px;
    color: var(--paper);
    font-weight: 700;
    font-size: 38px;
    letter-spacing: 0.5px;
  }
  .brand-mark__dot {
    width: 34px;
    height: 34px;
    border-radius: 50%;
    background: var(--paper);
  }
  .card--back {
    left: 628px;
    background: var(--paper);
  }
  .company-name {
    position: absolute;
    left: 36px;
    top: 32px;
    font-size: 21px;
    font-weight: 500;
    color: var(--brand-blue);
  }
  .info-block {
    position: absolute;
    left: 38px;
    padding-left: 14px;
    border-left: 2px solid var(--brand-blue);
  }
  .info-block--person { top: 92px; }
  .info-block--contact { top: 162px; }
  .person-name {
    font-size: 24px;
    font-weight: 700;
    color: var(--brand-blue);
    line-height: 1.15;
  }
  .person-title {
    font-size: 16px;
    color: var(--ink);
    margin-top: 6px;
  }
  .contact-line {
    font-size: 15.5px;
    color: var(--ink);
    line-height: 1.25;
  }
  .contact-line__label { display: inline-block; width: 52px; }
  .motto-band {
    position: absolute;
    left: 0;
    right: 0;
    bottom: 0;
    height: 62px;
    background: var(--brand-blue);
    color: var(--paper);
    font-size: 15px;
    font-weight: 500;
    text-align: center;
    line-height: 1.3;
    display: flex;
    align-items: center;
    justify-content: center;
  }
</style>
</head>
<body>
<main class="canvas">
  <section class="card card--front" aria-label="Card front">
    <div class="brand-mark">
      <span class="brand-mark__dot"></span>
      <span class="brand-mark__name">Tarvik Works</span>
    </div>
  </section>

  <section class="card card--back" aria-label="Card back">
    <h1 class="company-name">Tarvik Works, Inc.</h1>
    <div class="info-block info-block--person">
      <p class="person-name">Dana Whitlock</p>
      <p class="person-title">President and Chief EMC Engineer</p>
    </div>
    <div class="info-block info-block--contact">
      <p class="contact-line"><span class="contact-line__label">Email:</span>dana@tarvikworks.com</p>
      <p class="contact-line"><span class="contact-line__label">Web:</span>www.tarvikworks.com</p>
    </div>
    <p class="motto-band">We will solve your EMC problems as early as possible<br>- ideally before they even start.</p>
  </section>
</main>
</body>
</html>
```